7 Reeds Distillery - Bottle Label Design

We are a small craft distillery whose branding needs to incorporate our location on a lake (Lac Vorbelle, Quebec, Canada). A unique aspect of the lake is that people drive floating docks on the lake powered by a small outboard motor (see photos). Back in the 1970’s when Lac Vorbelle was a sparsely populated and difficult-to-access lake in the Gatineau Hills north of Ottawa, the concept of motorized docks was conjured on a lazy afternoon and this single stroke of genius has inadvertently spawned the most exceptional and eccentric lake based community. Throughout the summer, somewhere around four o’clock on any given Friday and Saturday it starts to happen. Docks set sail from their customary landing places - family, friends, snacks and loaded drink coolers in-tow and, as if magnetically drawn, head toward Heron Shoal. Without fail they will come upon a gathering of similar minded floating docks within the vicinity - be guided in with help to moor alongside and within seconds be seamlessly immersed in the festivities. Seldom any longer are these events planned, they have become elemental, a thing organically derived from within the community. This on-going weekly event is the genesis of the strong bond that brings us Seven Reeds Distilling.
Each of the 4 distillery owners have one of these docks so hence the name. We are open to either "7 Reeds" or spelled out as "Seven Reeds" as may be visually appropriate. We are also open to "Distillery" or "Distilling". More detail on the docks themselves, they are 14x16 feet powered by a small outboard motor as shown in the photos. This dock aspect may be difficult to incorporate into the branding but the lake outline is included as an image applicable to include for that local reference aspect. We will be creating very high quality small batch liquors such as vodka, rum, gin and whiskey. Each batch will be triple distilled and perhaps 20 bottles in quantity so very exclusive. We are aiming at a premium feel for the branding. Attached are some bottle label designs that evoke the type of feel we are going for and a photo of the style of blank bottle to design for which is a 750ml Nordic pattern bottle.
In general we are going for more contemporary than traditional, more bold than delicate. If a single label the size desired would be 4 inches wide and 4 inches tall. If a double/split label as in two of the photos the top label would be 3 inches wide and 3 inches tall and the bottom label would be max 4 inches wide and 1.5 inches tall. We are open to the upper label being a "transparent" label to create a printed on bottle effect, perhaps of the brand logo. We are only interested in front label so do not require a back, neck or closure label. The label will require the ability to name the batch style name (example "Tuberov") and then the amplifying information for the type of alcohol (Russian Potato Vodka) in a smaller font. Another example ("Bell Cap" and "London Dry Gin"). Information for bottle size (750ml) and alcohol % (40%) are also to be included. Governmental safety warnings are not required. We are open to use of any colours in the label. The basic label design would be re-used for different types of batches where we would change the style and alcohol name.

Target Market(s)

Up scale premium spirits buyers

Font styles to use
Serif
Sans Serif

Requirements
Must have
• A visual reference to the docks or the lake per the images attached.
Nice to have
• Ideally we can re-use the label design for a different type of Alcohol by changing the alcohol name and style information and maybe the colour of a major element in the label.

```html
<!DOCTYPE html>
<html lang="en">
<head>
<meta charset="utf-8">
<title>Seven Reeds Distillery – Tuberov Label</title>
<link rel="stylesheet" href="https://fonts.googleapis.com/css2?family=Oswald:wght@700&family=Merriweather:wght@900&family=Roboto:wght@400&family=Pinyon+Script&display=swap">
<style>
  :root {
    --ink: #1f1f1f;
    --brand-blue: #3b55a0;
    --lake-grey: #d3dbe2;
    --lake-grey-deep: #b8c3cd;
    --paper: #ffffff;
  }
  * { box-sizing: border-box; margin: 0; padding: 0; }
  html, body { width: 1200px; height: 848px; overflow: hidden; background: var(--paper); }
  .canvas { position: relative; width: 1200px; height: 848px; }

  /* Upper square label */
  .brand-label {
    position: absolute; left: 396px; top: 60px;
    width: 407px; height: 407px;
    border: 1.5px solid var(--ink);
  }
  .brand-mark {
    position: absolute; left: 170px; top: 48px;
    width: 200px; height: 200px; border-radius: 50%;
    background: var(--lake-grey);
  }
  .brand-name {
    position: absolute; left: 62px; top: 160px;
    font-family: "Oswald", sans-serif; font-weight: 700;
    color: var(--ink); text-transform: uppercase;
  }
  .brand-name .line { display: block; line-height: 1; }
  .brand-name .line-top { font-size: 58px; letter-spacing: 0.5px; }
  .brand-name .line-bottom { font-size: 68px; letter-spacing: 2px; margin-top: -4px; }
  .brand-descriptor {
    position: absolute; left: 62px; top: 296px;
    font-family: "Merriweather", serif; font-weight: 900;
    color: var(--brand-blue); font-size: 27px; letter-spacing: 5.5px;
    text-transform: uppercase; line-height: 1;
  }

  /* Lower band label */
  .batch-label { position: absolute; left: 232px; top: 520px; width: 736px; }
  .batch-main { display: flex; height: 80px; background: var(--lake-grey); }
  .motif-panel { width: 133px; display: flex; align-items: center; justify-content: center; gap: 12px; }
  .motif-placeholder { width: 38px; height: 62px; background: var(--lake-grey-deep); }
  .batch-centre {
    flex: 1; background: var(--paper); margin: 4px 0 0;
    display: flex; align-items: center;
  }
  .batch-meta {
    width: 102px; height: 62px; display: flex; flex-direction: column; justify-content: space-between;
    align-items: center; padding: 8px 0 6px;
    font-family: "Roboto", sans-serif; font-size: 10px; letter-spacing: 1.2px; color: var(--ink);
  }
  .rule-v { width: 1.5px; height: 66px; background: var(--ink); }
  .batch-title { flex: 1; text-align: center; }
  .style-name {
    font-family: "Merriweather", serif; font-weight: 900; color: var(--brand-blue);
    font-size: 36px; letter-spacing: 2px; line-height: 1;
  }
  .spirit-type {
    font-family: "Pinyon Script", cursive; color: var(--ink); font-size: 25px; line-height: 1.1;
  }
  .batch-note {
    width: 116px; text-align: center;
    font-family: "Roboto", sans-serif; font-size: 10px; letter-spacing: 1.2px; line-height: 14.5px;
    color: var(--ink); text-transform: uppercase;
  }
  .rule-h { height: 4px; background: var(--ink); margin-top: 2px; }
  .spec-bar {
    height: 24px; margin-top: 5px; background: var(--ink); color: var(--paper);
    display: flex; align-items: center; justify-content: space-around;
    font-family: "Roboto", sans-serif; font-size: 11.5px; letter-spacing: 1.6px; text-transform: uppercase;
  }
</style>
</head>
<body>
<div class="canvas">

  <section class="brand-label">
    <span class="brand-mark"></span>
    <div class="brand-name">
      <span class="line line-top">Seven</span>
      <span class="line line-bottom">Reeds</span>
    </div>
    <div class="brand-descriptor">Distillery</div>
  </section>

  <section class="batch-label">
    <div class="batch-main">
      <div class="motif-panel">
        <div class="motif-placeholder" role="img" aria-label="Outline outboard motor icon"></div>
        <div class="motif-placeholder" role="img" aria-label="Solid outboard motor icon"></div>
      </div>
      <div class="batch-centre">
        <div class="batch-meta"><span>BOTTLE N.</span><span>BATCH:</span></div>
        <div class="rule-v"></div>
        <div class="batch-title">
          <div class="style-name">TUBEROV</div>
          <div class="spirit-type">Russian Potato Vodka</div>
        </div>
        <div class="rule-v"></div>
        <div class="batch-note">Crafted with<br>artisan drawn<br>Lac Vorbelle<br>lake water</div>
      </div>
      <div class="motif-panel">
        <div class="motif-placeholder" role="img" aria-label="Solid outboard motor icon"></div>
        <div class="motif-placeholder" role="img" aria-label="Solid outboard motor icon"></div>
      </div>
    </div>
    <div class="rule-h"></div>
    <div class="spec-bar">
      <span>· Handcrafted ·</span>
      <span>40% ABV ★★ Triple Distilled ★★ 750 ML</span>
      <span>· Small Batch ·</span>
    </div>
  </section>

</div>
</body>
</html>
```